Company Vehicle design

We have a Green, 2014 Torvik Hauler w/ Windows (photo attached) that we would like to design a logo scheme for. We are not interested in a full wrap, but would like a simple, tasteful die-cut sticker based design for the vehicle. We would like to incorporate the two attached logos, with the Brightcrest Outfitters logo (either layout) being the primary, and the Marlow Ridgeway Climbs logo being the secondary. Some design on the windows is ok, but we do not want visibility obscured. I've also attached a photo of another company vehicle that we like (red truck) as well as an old company vehicle that we do not like (white van, way too much going on, we like simple)!

Colors

Designer to choose colors to be used in the design.

Requirements
Must have
• Please include both logos provided.
Nice to have
• Website: www.brightcrestoutfitters.com
• Phone: 877-555-0142
Should not have
• A complicated design that feels busy.

```html
<!DOCTYPE html>
<html lang="en">
<head>
<meta charset="utf-8">
<title>Brightcrest Outfitters – Torvik Hauler Decal Set</title>
<link rel="stylesheet" href="https://fonts.googleapis.com/css2?family=Questrial&family=Roboto+Condensed:wght@700&display=swap">
<style>
  :root {
    --ground: #000000;
    --ink: #ffffff;
    --divider: #8a8a8a;
    --display: "Questrial", "Helvetica Neue", Arial, sans-serif;
    --condensed: "Roboto Condensed", "Arial Narrow", sans-serif;
  }
  * { margin: 0; padding: 0; box-sizing: border-box; }
  html, body {
    width: 1200px; height: 879px; overflow: hidden;
    background: var(--ground);
  }
  .decal-sheet {
    position: relative; width: 1200px; height: 879px;
    background: var(--ground); color: var(--ink);
    display: flex;
  }
  .side-decal { position: relative; width: 900px; height: 879px; }
  .side-decal svg { display: block; }
  .side-decal text { fill: var(--ink); }
  .side-phone { font-family: var(--condensed); font-weight: 700; font-size: 84px; }
  .side-web { font-family: var(--condensed); font-weight: 700; font-size: 27px; }
  .side-name { font-family: var(--display); font-size: 98px; letter-spacing: 1px; }
  .side-tagline { font-family: var(--display); font-size: 58px; letter-spacing: 12px; }
  .rule { stroke: var(--ink); stroke-width: 2.5; fill: none; }

  .secondary-mark {
    position: absolute; display: flex; align-items: center; gap: 10px;
    font-family: var(--display); color: var(--ink); text-transform: uppercase;
    letter-spacing: 3px; line-height: 1.25;
  }
  .secondary-mark .mark-square { border: 2px solid var(--ink); flex: none; }
  .side-decal .secondary-mark { left: 690px; top: 585px; font-size: 17px; }
  .side-decal .mark-square { width: 22px; height: 22px; }

  .rear-decal {
    width: 300px; height: 879px; border-left: 2px solid var(--divider);
    display: flex; flex-direction: column; align-items: center; justify-content: center;
    text-align: center;
  }
  .rear-name { font-family: var(--display); font-size: 37px; letter-spacing: 1px; line-height: 1; }
  .rear-tagline { font-family: var(--display); font-size: 27px; letter-spacing: 6px; margin-top: 8px; }
  .rear-phone { font-family: var(--condensed); font-weight: 700; font-size: 38px; margin-top: 40px; line-height: 1; }
  .rear-web { font-family: var(--condensed); font-weight: 700; font-size: 13px; margin-top: 4px; }
  .rear-decal .secondary-mark { position: static; margin-top: 22px; font-size: 9px; letter-spacing: 2px; gap: 6px; }
  .rear-decal .mark-square { width: 12px; height: 12px; }
</style>
</head>
<body>
<main class="decal-sheet">
  <section class="side-decal" aria-label="Side panel decal">
    <svg width="900" height="879" viewBox="0 0 900 879">
      <g transform="translate(450 430) rotate(-12)">
        <line class="rule" x1="-170" y1="-320" x2="-170" y2="-250"/>
        <text class="side-phone" x="-215" y="-160">877-555-0142</text>
        <text class="side-web" x="-215" y="-128">www.brightcrestoutfitters.com</text>
        <line class="rule" x1="140" y1="-146" x2="470" y2="-146"/>
        <text class="side-name" x="-400" y="40">BRIGHTCREST</text>
        <text class="side-tagline" x="395" y="120" text-anchor="end">outfitters</text>
        <line class="rule" x1="-440" y1="138" x2="-70" y2="138"/>
        <line class="rule" x1="110" y1="80" x2="110" y2="240"/>
      </g>
    </svg>
    <div class="secondary-mark">
      <span class="mark-square"></span>
      <span>Marlow Ridgeway<br>Climbs</span>
    </div>
  </section>

  <section class="rear-decal" aria-label="Rear door decal">
    <div class="rear-name">BRIGHTCREST</div>
    <div class="rear-tagline">outfitters</div>
    <div class="rear-phone">877-555-0142</div>
    <div class="rear-web">www.brightcrestoutfitters.com</div>
    <div class="secondary-mark">
      <span class="mark-square"></span>
      <span>Marlow Ridgeway<br>Climbs</span>
    </div>
  </section>
</main>
</body>
</html>
```